Creating a label for germicidal disposable wipes.

I need to create a label to put on our containers of germicidal disposable wipes. I am attaching an example of another germicidal wipe that I would like a similar format but more customized to look like my companies.

```html
<!DOCTYPE html>
<html lang="en">
<head>
<meta charset="utf-8">
<title>NVC Summit Large Wipe Label</title>
<link href="https://fonts.googleapis.com/css2?family=Roboto+Condensed:ital,wght@0,400;0,500;0,700;1,400&family=Oswald:wght@500;700&display=swap" rel="stylesheet">
<style>
  :root {
    --navy: #1e2a7c;
    --navy-deep: #17206a;
    --green: #22b04b;
    --green-soft: #2fbf5a;
    --grey: #5a5a5a;
    --grey-dark: #3a3a3a;
    --white: #ffffff;
    --page: #eceef1;
  }
  * { box-sizing: border-box; margin: 0; padding: 0; }
  html, body { width: 1200px; height: 1200px; overflow: hidden; }
  body {
    background: var(--page);
    font-family: "Roboto Condensed", "Arial Narrow", sans-serif;
    position: relative;
  }
  .label {
    position: absolute; left: 50px; top: 124px;
    width: 1100px; height: 952px;
    background: var(--white);
    border-radius: 14px 22px 22px 14px;
    overflow: hidden;
    box-shadow: 0 4px 18px rgba(0,0,0,.12);
  }
  .brand {
    position: absolute; left: 42px; top: 60px;
    display: flex; align-items: center; gap: 16px;
  }
  .brand-dot { width: 96px; height: 96px; border-radius: 50%; background: var(--navy); }
  .brand-text { display: flex; flex-direction: column; }
  .brand-name { font-weight: 700; font-size: 74px; line-height: .95; color: var(--grey-dark); }
  .brand-division { font-weight: 700; font-size: 20px; color: var(--grey-dark); letter-spacing: .5px; }
  .brand-full { font-weight: 700; font-size: 20px; color: var(--grey-dark); letter-spacing: .3px; }

  .product-tab {
    position: absolute; left: 504px; top: 10px;
    width: 203px; height: 211px;
    background: var(--navy);
    border-top: 42px solid var(--green);
    color: var(--white);
    text-align: center;
  }
  .product-name {
    font-family: "Oswald", sans-serif; font-weight: 700;
    font-size: 54px; line-height: 1; margin-top: 14px;
  }
  .product-rule { width: 150px; height: 3px; background: var(--white); margin: 8px auto 8px; }
  .product-size { font-weight: 500; font-size: 24px; letter-spacing: .5px; }

  .steps { position: absolute; left: 42px; top: 245px; width: 600px; height: 190px; }
  .steps-line { position: absolute; left: 80px; top: 76px; width: 420px; height: 3px; background: var(--grey); }
  .step { position: absolute; top: 0; width: 200px; text-align: center; }
  .step-icon {
    width: 152px; height: 152px; margin: 0 auto; border-radius: 50%;
    border: 5px solid var(--grey); background: var(--white);
    display: flex; align-items: center; justify-content: center; position: relative;
  }
  .step-core {
    width: 130px; height: 130px; border-radius: 50%; background: var(--grey);
    display: flex; flex-direction: column; align-items: center; justify-content: center; color: var(--white);
  }
  .step-num { font-family: "Oswald", sans-serif; font-weight: 700; font-size: 70px; line-height: .9; }
  .step-unit { font-weight: 500; font-size: 20px; }
  .step-caption { margin-top: 14px; font-size: 18px; font-weight: 500; color: var(--grey-dark); }

  .claim {
    position: absolute; left: 42px; top: 466px;
    font-weight: 700; font-size: 23px; color: var(--navy); letter-spacing: .2px;
  }
  .ingredients { position: absolute; left: 42px; top: 512px; width: 600px; }
  .ingredients-title {
    font-weight: 700; font-size: 24px; color: var(--green);
    text-decoration: underline; text-underline-offset: 3px; margin-bottom: 12px;
  }
  .ingredient-row {
    display: flex; align-items: baseline; font-size: 22px; color: var(--grey-dark); height: 32px;
  }
  .ingredient-dots { flex: 1; border-bottom: 2px dotted var(--grey-dark); margin: 0 4px; transform: translateY(-5px); }
  .ingredients-note { font-style: italic; font-size: 19px; color: var(--grey-dark); margin-top: 8px; }

  .warning-band {
    position: absolute; left: 0; top: 735px; width: 731px; height: 172px;
    background: var(--navy); color: var(--white); padding: 10px 0 0 42px;
  }
  .keep-out { font-family: "Oswald", sans-serif; font-weight: 500; font-size: 29px; color: var(--green-soft); line-height: 1.1; }
  .warning-line { display: flex; align-items: center; gap: 10px; margin-top: 2px; }
  .warning-word { font-family: "Oswald", sans-serif; font-weight: 700; font-size: 44px; line-height: 1; }
  .warning-note { font-size: 18px; line-height: 1.05; }
  .contents { font-size: 30px; font-weight: 500; margin-top: 4px; }
  .contents small { font-size: 16px; }
  .net-wt { font-size: 15px; }
  .band-mark {
    position: absolute; right: 70px; top: 22px;
    display: flex; align-items: center; gap: 10px;
  }
  .band-mark-dot { width: 110px; height: 110px; border-radius: 50%; background: var(--green); opacity: .85; }

  .info-panel {
    position: absolute; left: 731px; top: 0; width: 369px; height: 952px;
    background: linear-gradient(90deg, var(--green) 0%, #1f7a6a 50%, var(--navy-deep) 100%);
    color: var(--white); padding: 48px 28px 0 40px;
  }
  .info-title { font-weight: 700; font-size: 24px; margin-bottom: 18px; }
  .info-text { font-size: 14.5px; font-weight: 700; line-height: 1.3; margin-bottom: 18px; }
  .info-text strong { font-size: 20px; font-weight: 500; }
</style>
</head>
<body>
<main class="label">
  <div class="brand">
    <span class="brand-dot"></span>
    <div class="brand-text">
      <span class="brand-name">NVC</span>
      <span class="brand-division">HAZARDOUS DIVISION</span>
      <span class="brand-full">NORTHVALE CLINICAL SERVICES</span>
    </div>
  </div>

  <div class="product-tab">
    <div class="product-name">SUMMIT</div>
    <div class="product-rule"></div>
    <div class="product-size">LARGE WIPE</div>
  </div>

  <section class="steps">
    <div class="steps-line"></div>
    <div class="step" style="left:-20px">
      <div class="step-icon"><div class="step-core"><span class="step-num">2</span><span class="step-unit">MINUTES</span></div></div>
      <div class="step-caption">DISINFECTS IN</div>
    </div>
    <div class="step" style="left:178px">
      <div class="step-icon"><div class="step-core" role="img" aria-label="Hand wiping icon"></div></div>
      <div class="step-caption">NOT A SKIN OR BABY WIPE</div>
    </div>
    <div class="step" style="left:380px">
      <div class="step-icon">
        <div class="step-core">
          <svg width="70" height="80" viewBox="0 0 70 80" role="img" aria-label="Toilet icon">
            <rect x="8" y="4" width="20" height="34" rx="3" fill="#fff"/>
            <path d="M4 40 H62 Q62 60 40 62 L44 76 H18 L22 62 Q4 58 4 40 Z" fill="#fff"/>
          </svg>
        </div>
      </div>
      <div class="step-caption">DO NOT FLUSH</div>
    </div>
  </section>

  <p class="claim">BACTERICIDAL, TUBERCULOCIDAL, AND VIRUCIDAL * IN 2 MINUTES</p>

  <section class="ingredients">
    <h2 class="ingredients-title">ACTIVE INGREDIENTS</h2>
    <div class="ingredient-row"><span>BACTERICIDAL,</span><span class="ingredient-dots"></span><span>05%</span></div>
    <div class="ingredient-row"><span>TUBERCULOCIDAL</span><span class="ingredient-dots"></span><span>05%</span></div>
    <div class="ingredient-row"><span>VIRUCIDAL</span><span class="ingredient-dots"></span><span>05%</span></div>
    <div class="ingredient-row"><span>BACTERICIDAL,</span><span class="ingredient-dots"></span><span>05%</span></div>
    <p class="ingredients-note">Does not icludie the weight of thr wipe</p>
  </section>

  <section class="warning-band">
    <div class="keep-out">KEEP OUT OF REACH OF CHILDREN</div>
    <div class="warning-line">
      <span class="warning-word">WARNING</span>
      <span class="warning-note">See back panel for additional<br>precautionary statements</span>
    </div>
    <div class="contents">Contains: 160 wipes <small>6x6.75in (15.2 x 17.1cm)</small></div>
    <div class="net-wt">Net Wt. 1 lb 13 oz (833g)</div>
    <div class="band-mark"><span class="band-mark-dot"></span></div>
  </section>

  <aside class="info-panel">
    <h2 class="info-title">Title Here:</h2>
    <p class="info-text"><strong>Lorem ipsum</strong> dolor sit amet, consectetuer adipiscing elit, sed diam nonummy nibh euismod tincidunt ut laoreet dolore magna aliquam erat volutpat. Ut wisi enim ad minim veniam, quis nostrud exerci tation ullamcorper suscipit lobortis nisl ut aliquip ex ea commodo consequat. Duis autem vel eum iriure dolor in hendrerit in vulputate velit esse molestie consequat, vel illum dolore eu feugiat nulla facilisis at vero eros et accumsan et iusto odio dignissim qui blandit praesent luptatum zzril delenit augue duis dolore te feugait nulla facilisi.</p>
    <p class="info-text"><strong>Lorem ipsum</strong> dolor sit amet, cons ectetuer adipiscing elit, sed diam nonummy nibh euismod tincidunt ut laoreet dolore magna aliquam erat volutpat. Ut wisi enim ad minim veniam, quis nostrud exerci tation ullamcorper suscipit lobortis nisl ut aliquip ex ea commodo consequat. Lorem ipsum dolor sit amet, consectetuer adipiscing elit, sed diam nonummy nibh euismod tincidunt ut laoreet dolore magna aliquam erat volutpat. Ut wisi enim ad minim veniam, quis nostrud exerci tation ullamcorper suscipit lobortis nisl ut aliquip ex ea commodo consequat. Duis autem vel eum iriure dolor in hendrerit in vulputate velit esse molestie consequat, vel illum dolore eu feugiat nulla facilisis at vero eros et accumsan et iusto odio dignissim qui blandit praesent luptatum zzril delenit augue duis dolore te feugait nulla facilisi.</p>
    <p class="info-text"><strong>Lorem ipsum</strong> dolor sit amet, cons ectetuer adipiscing elit, sed diam nonummy nibh euismod tincidunt ut laoreet dolore magna aliquam erat volutpat. Ut wisi enim ad minim veniam, quis nostrud exerci tation ullamcorper suscipit lobortis nisl ut aliquip ex ea commodo consequat.</p>
  </aside>
</main>
</body>
</html>
```